Civora Website

We are a newly formed Real Estate Development Company based in New York. We develop affordable housing apartments. We partner up with private and non profit companies in NY. We would like to have a clean website that relates to our new logo. The target market are individuals that own large parcels of land, churches and private investors and individuals. The final design should communicate financial safety, caring for the community, power and humbleness. Additionally, the website has to be capable to seen in smartphones and the designer has to upload it our hostwren hosting account. The site is going to have around 16 topics. For example: a home page, about us, mission, how we work, our work, building affordable communities, two examples on gentrification, community based planning, Real Estate Consulting, Real Estate Development, Financing/Partnerships, Recruiting, contact page.
See our logo attached.

Target Market(s)

Community leaders, politicians, investors, land owners, activists, real estate brokers, government agencies, other developers,

Industry/Entity Type

Non Profit

Number of Pages Required

1 page

Font styles to use
Sans Serif

Requirements
Must have
• Pictures of buildings from NYC. Facades, lobby, a family in a building, it can be in some cases a combination of sketchers and actual pictures. Clean website.
• People will be able to see it in both desktop and smartphones. The contact page with our information and also to be contacted via email.

```html
<!DOCTYPE html>
<html lang="en">
<head>
<meta charset="utf-8">
<title>Civora Community Development</title>
<link href="https://fonts.googleapis.com/css2?family=Open+Sans:ital,wght@0,400;0,600;0,700;1,400;1,600&display=swap" rel="stylesheet">
<style>
  :root {
    --green: #34b233;
    --blue: #0d3fa3;
    --blue-deep: #0a3590;
    --ink: #1a1a1a;
    --text: #444;
    --gray-band: #efefef;
    --white: #fff;
    --field-border: #c9c9c9;
  }
  * { box-sizing: border-box; margin: 0; padding: 0; }
  html, body { width: 782px; height: 1200px; overflow: hidden; background: var(--white); }
  body { position: relative; font-family: "Open Sans", Arial, sans-serif; color: var(--text); }
  .abs { position: absolute; }

  /* header */
  .site-header { left: 0; top: 0; width: 782px; height: 108px; }
  .brand { left: 0; width: 782px; top: 34px; text-align: center; }
  .brand-name { font-size: 32px; font-weight: 600; color: var(--blue); line-height: 40px; }

  /* navigation */
  .main-nav { left: 0; top: 108px; width: 782px; height: 36px; background: var(--green); display: flex; justify-content: center; align-items: center; font-size: 8.2px; color: var(--white); }
  .main-nav a { color: var(--white); text-decoration: none; }
  .main-nav a.active { color: var(--blue); text-decoration: underline; }
  .main-nav .sep { margin: 0 9px; }

  /* hero */
  .hero { left: 0; top: 144px; width: 782px; height: 290px; overflow: hidden; }
  .hero svg { position: absolute; left: 0; top: 0; }
  .hero-copy { left: 48px; top: 50px; width: 245px; color: var(--white); }
  .hero-title { font-size: 19px; font-style: italic; font-weight: 400; white-space: nowrap; }
  .hero-sub { font-size: 12.5px; font-style: italic; margin-top: 6px; }
  .hero-lead { font-size: 12px; font-style: italic; margin-top: 6px; }
  .hero-text { font-size: 7.4px; line-height: 13.5px; margin-top: 6px; }
  .btn-green { left: 48px; top: 198px; width: 82px; height: 26px; background: var(--green); color: var(--white); font-size: 9px; font-weight: 600; display: flex; align-items: center; justify-content: center; }
  .slider-dots { left: 48px; top: 246px; display: flex; gap: 4px; }
  .slider-dots span { width: 8px; height: 8px; border-radius: 50%; background: rgba(255,255,255,.45); }
  .slider-dots span.on { background: var(--white); }

  /* sections */
  .section-title { font-size: 17px; font-weight: 600; color: var(--ink); text-align: center; }
  .section-text { font-size: 7.4px; line-height: 13.5px; text-align: center; color: var(--text); }
  .welcome { left: 0; top: 434px; width: 782px; height: 78px; }
  .welcome .section-title { margin-top: 14px; }
  .welcome .section-text { width: 460px; margin: 4px auto 0; }

  .properties { left: 0; top: 512px; width: 782px; height: 286px; background: var(--gray-band); }
  .properties .section-title { margin-top: 13px; }
  .properties .section-text { width: 460px; margin: 4px auto 0; }
  .property-card { top: 80px; width: 159px; }
  .property-head { height: 22px; background: var(--green); color: var(--white); font-size: 7.4px; display: flex; align-items: center; justify-content: center; }
  .property-photo { height: 93px; }
  .property-text { font-size: 7.4px; line-height: 13.5px; text-align: center; margin-top: 11px; }
  .btn-blue { width: 74px; height: 21px; background: var(--blue); color: var(--white); font-size: 7.6px; display: flex; align-items: center; justify-content: center; margin: 11px auto 0; border-radius: 2px; }

  .gallery-title, .contact-title { font-size: 17px; font-weight: 600; color: var(--ink); }
  .gallery-title { left: 64px; top: 815px; }
  .gallery-text { left: 64px; top: 840px; width: 260px; font-size: 7.4px; line-height: 13.5px; }
  .thumb { width: 96px; height: 84px; }
  .view-all { left: 64px; top: 1075px; font-size: 8.6px; font-weight: 700; color: var(--blue); text-decoration: underline; }

  .contact-title { left: 522px; top: 815px; }
  .field { left: 526px; width: 165px; height: 29px; border: 1px solid var(--field-border); background: var(--white); font-size: 7.2px; color: #555; padding: 0 9px; display: flex; align-items: center; }
  .field.message { height: 77px; align-items: flex-start; padding-top: 9px; }
  .btn-submit { left: 526px; top: 1065px; width: 75px; height: 24px; background: linear-gradient(#1f55b8, var(--blue-deep)); color: var(--white); font-size: 7.6px; font-weight: 600; display: flex; align-items: center; justify-content: center; border-radius: 4px; }

  /* footer */
  .site-footer { left: 0; top: 1124px; width: 782px; height: 76px; background: var(--green); color: var(--white); }
  .footer-nav { left: 64px; top: 22px; font-size: 6.8px; }
  .footer-nav .sep { margin: 0 7px; }
  .footer-copy { left: 64px; top: 37px; font-size: 6.8px; }
  .social { top: 23px; width: 17px; height: 17px; background: var(--white); border-radius: 3px; }
</style>
</head>
<body>

<header class="site-header abs">
  <div class="brand abs">
    <div class="brand-name">Civora Community Development</div>
  </div>
</header>

<nav class="main-nav abs">
  <a class="active">Home</a><span class="sep">I</span>
  <a>About us</a><span class="sep">I</span>
  <a>Mission</a><span class="sep">I</span>
  <a>Work</a><span class="sep">I</span>
  <a>Gentrification</a><span class="sep">I</span>
  <a>Planning</a><span class="sep">I</span>
  <a>Consulting</a><span class="sep">I</span>
  <a>Partnerships</a><span class="sep">I</span>
  <a>Recruiting</a><span class="sep">I</span>
  <a>Contact</a>
</nav>

<section class="hero abs">
  <svg width="782" height="290" viewBox="0 0 782 290">
    <defs>
      <linearGradient id="skyline" x1="0" y1="0" x2="0" y2="1">
        <stop offset="0" stop-color="#8fb3d9"/>
        <stop offset=".45" stop-color="#b59a7e"/>
        <stop offset=".8" stop-color="#7a6a5c"/>
        <stop offset="1" stop-color="#4d6578"/>
      </linearGradient>
      <linearGradient id="panel" x1="0" y1="0" x2="1" y2="1">
        <stop offset="0" stop-color="#1446b0"/>
        <stop offset="1" stop-color="#0b3592"/>
      </linearGradient>
    </defs>
    <rect width="782" height="290" fill="url(#skyline)" role="img" aria-label="Photo of the New York City skyline across the river"/>
    <path d="M0,0 H263 Q368,145 255,290 H0 Z" fill="url(#panel)"/>
    <path d="M263,0 Q368,145 255,290" fill="none" stroke="var(--green)" stroke-width="4"/>
  </svg>
  <div class="hero-copy abs">
    <h1 class="hero-title">SELL YOUR HOUSE FASTER</h1>
    <p class="hero-sub">AT THE HIGHEST POSSIBLE PRICE !</p>
    <p class="hero-lead">Preparing your residence for sale</p>
    <p class="hero-text">Fusce euismod consequat ante. Lorem ipsum dolor sit amet, consectetuer. Pellentesque sed dolor. Aliquam congue fermentum nisl. Mauris accumsan nulla vel diam. Sed in lacus ut enim adipiscing aliquet. Nulla venenatis.</p>
  </div>
  <div class="btn-green abs">MORE INFO</div>
  <div class="slider-dots abs"><span></span><span></span><span></span><span class="on"></span></div>
</section>

<section class="welcome abs">
  <h2 class="section-title">WELCOME !!!</h2>
  <p class="section-text">Sed in lacus ut enim adipiscing aliquet. Nulla venenatis. In pede mi, aliquet sit amet, euismod in, auctor ut, ligula. Aliquam dapibus tincidunt metus. Praesent justo dolor, lobortis quis, lobortis dignissim, pulvinar ac, lorem. Vestibulum sed ante.</p>
</section>

<section class="properties abs">
  <h2 class="section-title">RECENTLY ADDED PROPERTIES</h2>
  <p class="section-text">Sed in lacus ut enim adipiscing aliquet. Nulla venenatis. In pede mi, aliquet sit amet, euismod in, auctor ut, ligula. Aliquam dapibus tincidunt metus. Praesent justo dolor, lobortis quis, lobortis dignissim, pulvinar ac, lorem. Vestibulum sed ante.</p>

  <article class="property-card abs" style="left:64px">
    <div class="property-head">FUSCE EUISMOD CONSEQUAT ANTE</div>
    <div class="property-photo" role="img" aria-label="Photo of a bright modern living room" style="background:linear-gradient(135deg,#d8d2c8,#6b625a)"></div>
    <p class="property-text">Neque porro quisquam est, qui dolorem ipsum quia dolor sit amet consectetur</p>
    <div class="btn-blue">READ MORE</div>
  </article>
  <article class="property-card abs" style="left:229px">
    <div class="property-head">PELLENTESQUE SED DOLOR</div>
    <div class="property-photo" role="img" aria-label="Photo of historic brick building facades" style="background:linear-gradient(135deg,#c8b8a8,#7a4a34)"></div>
    <p class="property-text">Neque porro quisquam est, qui dolorem ipsum quia dolor sit amet consectetur</p>
    <div class="btn-blue">READ MORE</div>
  </article>
  <article class="property-card abs" style="left:394px">
    <div class="property-head">ENIM ADIPISCING ALIQUET</div>
    <div class="property-photo" role="img" aria-label="Photo of a smiling family at home" style="background:linear-gradient(135deg,#e6e2dc,#a98c74)"></div>
    <p class="property-text">Neque porro quisquam est, qui dolorem ipsum quia dolor sit amet consectetur</p>
    <div class="btn-blue">READ MORE</div>
  </article>
  <article class="property-card abs" style="left:559px">
    <div class="property-head">MAURIS ACCUMSAN NULLA</div>
    <div class="property-photo" role="img" aria-label="Photo of a new stone and brick storefront building" style="background:linear-gradient(180deg,#a9c4e4,#9a7a62 60%,#7d8a64)"></div>
    <p class="property-text">Neque porro quisquam est, qui dolorem ipsum quia dolor sit amet consectetur</p>
    <div class="btn-blue">READ MORE</div>
  </article>
</section>

<h2 class="gallery-title abs">GALLERY</h2>
<p class="gallery-text abs">Sed in lacus ut enim adipiscing aliquet. Nulla venenatis. In pede mi, tincidunt metus. Praesent justo dolor, lobortis Vestibulum sed ante.</p>
<div class="thumb abs" style="left:64px;top:882px;background:linear-gradient(135deg,#7a5a42,#3a2a1e)" role="img" aria-label="Photo of a warm bedroom interior"></div>
<svg class="abs" style="left:106px;top:918px" width="13" height="13" viewBox="0 0 13 13"><path d="M6.5 0V13M0 6.5H13" stroke="#fff" stroke-width="1.6"/></svg>
<div class="thumb abs" style="left:165px;top:882px;background:linear-gradient(180deg,#c9d6e6,#a9a39a 55%,#6f7d55)" role="img" aria-label="Photo of a two storey suburban house"></div>
<div class="thumb abs" style="left:266px;top:882px;background:linear-gradient(180deg,#5a6070,#c79a5a 55%,#2b4b6a)" role="img" aria-label="Photo of a modern house with a pool at dusk"></div>
<div class="thumb abs" style="left:368px;top:882px;background:linear-gradient(180deg,#8fb0d8,#7a7570 60%,#4f6b3a)" role="img" aria-label="Photo of a contemporary grey house"></div>
<div class="thumb abs" style="left:64px;top:972px;background:linear-gradient(180deg,#a8c6e8,#d8d4cc 60%,#7a8a5a)" role="img" aria-label="Photo of a single storey house"></div>
<div class="thumb abs" style="left:165px;top:972px;background:linear-gradient(180deg,#d8d8d8,#8a4a34 50%,#4e5a34)" role="img" aria-label="Photo of a red brick house"></div>
<div class="thumb abs" style="left:266px;top:972px;background:linear-gradient(180deg,#324a66,#b8c8d8 55%,#3a8aa8)" role="img" aria-label="Photo of a glass villa with a pool"></div>
<div class="thumb abs" style="left:368px;top:972px;background:linear-gradient(180deg,#b8cce4,#3a4654 45%,#c8c4bc)" role="img" aria-label="Photo of a house with a white porch"></div>
<a class="view-all abs">VIEW ALL</a>

<h2 class="contact-title abs">CONTACT US</h2>
<div class="field abs" style="top:855px">NAME</div>
<div class="field abs" style="top:894px">EMAIL ADDRESS</div>
<div class="field abs" style="top:934px">PHONE NUMBER (OPTIONAL )</div>
<div class="field message abs" style="top:973px">MESSAGE</div>
<div class="btn-submit abs">SUBMIT</div>

<footer class="site-footer abs">
  <div class="footer-nav abs">Home<span class="sep">I</span>About us<span class="sep">I</span>mission<span class="sep">I</span>work<span class="sep">I</span>gentrification<span class="sep">I</span>Planning<span class="sep">I</span>Consulting<span class="sep">I</span>Partnerships<span class="sep">I</span>Recruiting<span class="sep">I</span>Contact</div>
  <div class="footer-copy abs">Civora Community Development © 2015 Privacy policy</div>
  <span class="social abs" style="left:644px"></span>
  <span class="social abs" style="left:672px"></span>
  <span class="social abs" style="left:700px"></span>
</footer>

</body>
</html>
```